Business Card Design

We need a business card design for a new dental practice in Brisbane. I'd like the basic details and logo on one side and appointment schedule on the other side. It is based in CBD office area and would prefer a professional and modern design.
Target Market(s)
20-60 years old office workers and residents with high education levels
Industry/Entity Type
Dental
Contact Information for Business Card
Harbourlight Dental
Dr Glenn Marwick
Principal Dentist
07 3964 2275
admin@harbourlightsmiles.com.au
www.harbourlightsmiles.com.au
S27, Level 3, Ardent North Plaza, 814 Tallowood Rd, Kelsey Heights, QLD 4019

```html
<!DOCTYPE html>
<html lang="en">
<head>
<meta charset="utf-8">
<title>Harbourlight Dental – Business Card</title>
<link href="https://fonts.googleapis.com/css2?family=Questrial&family=Open+Sans:wght@400;600&display=swap" rel="stylesheet">
<style>
  :root {
    --page-bg: #e9ebee;
    --card-bg: #ffffff;
    --ink: #1f2a36;
    --ink-soft: #3c4650;
    --accent: #3aa3d9;
    --rule: #5a626b;
    --shade: #dfe3e8;
  }
  * { box-sizing: border-box; margin: 0; padding: 0; }
  html, body { width: 1200px; height: 784px; overflow: hidden; }
  body {
    background: var(--page-bg);
    font-family: "Open Sans", Arial, sans-serif;
    color: var(--ink);
    position: relative;
  }
  .card {
    position: absolute;
    width: 600px;
    height: 340px;
    background: var(--card-bg);
    box-shadow: 0 6px 18px rgba(0,0,0,0.12);
    overflow: hidden;
  }
  .card--back { left: 60px; top: 46px; }
  .card--front { left: 540px; top: 408px; }

  .card__shade {
    position: absolute;
    inset: 0;
    background: linear-gradient(100deg, var(--shade) 0%, rgba(223,227,232,0) 38%);
  }
  .card--front .card__shade {
    background: linear-gradient(260deg, var(--shade) 0%, rgba(223,227,232,0) 34%);
  }

  /* appointment side */
  .appointment__title {
    position: absolute;
    top: 32px; left: 0; right: 0;
    text-align: center;
    font-size: 17px;
    font-weight: 400;
    color: var(--ink-soft);
  }
  .field {
    position: absolute;
    display: flex;
    align-items: baseline;
    font-size: 16px;
    color: var(--ink-soft);
  }
  .field__line {
    flex: 1;
    margin-left: 8px;
    border-bottom: 2px dotted var(--rule);
    height: 1px;
  }
  .field--top  { top: 64px; left: 350px; width: 222px; }
  .field--top .field__line { margin-left: 0; }
  .field--name { top: 96px; left: 36px; width: 290px; }
  .field--time { top: 90px; left: 350px; width: 222px; }
  .field--date { top: 138px; left: 44px; width: 282px; }

  .brand {
    position: absolute;
    display: flex;
    align-items: center;
    gap: 10px;
    font-family: "Questrial", Arial, sans-serif;
    color: var(--ink);
    white-space: nowrap;
  }
  .brand__dot {
    border-radius: 50%;
    background: var(--accent);
    flex: none;
  }
  .card--back .brand { right: 28px; bottom: 28px; font-size: 20px; }
  .card--back .brand__dot { width: 16px; height: 16px; }

  /* front side */
  .dentist {
    position: absolute;
    top: 22px; right: 26px;
    text-align right;
    text-align: right;
  }
  .dentist__name { font-size: 16px; color: var(--ink); }
  .dentist__role { font-size: 11px; color: var(--accent); }

  .card--front .brand { left: 40px; top: 104px; font-size: 40px; }
  .card--front .brand__dot { width: 28px; height: 28px; }

  .contact {
    position: absolute;
    left: 40px; bottom: 24px;
    list-style: none;
    font-size: 15px;
    line-height: 1.35;
    color: var(--ink);
  }
  .contact__item { display: flex; align-items: flex-start; gap: 8px; }
  .contact__icon { width: 16px; height: 16px; flex: none; margin-top: 3px; fill: var(--accent); }
</style>
</head>
<body>

  <section class="card card--back" aria-label="Appointment side">
    <div class="card__shade"></div>
    <h2 class="appointment__title">Appointment</h2>
    <div class="field field--top"><span class="field__line"></span></div>
    <div class="field field--name">Name:<span class="field__line"></span></div>
    <div class="field field--time">Time :<span class="field__line"></span></div>
    <div class="field field--date">Date &nbsp;:<span class="field__line"></span></div>
    <div class="brand"><span class="brand__dot"></span>Harbourlight Dental</div>
  </section>

  <section class="card card--front" aria-label="Contact side">
    <div class="card__shade"></div>
    <div class="dentist">
      <p class="dentist__name">Dr Glenn Marwick</p>
      <p class="dentist__role">Principal Dentist</p>
    </div>
    <div class="brand"><span class="brand__dot"></span>Harbourlight Dental</div>
    <ul class="contact">
      <li class="contact__item">
        <svg class="contact__icon" viewBox="0 0 16 16" aria-hidden="true"><path d="M3 1l3 3-1.5 2a9 9 0 0 0 5.5 5.5L12 10l3 3-2 2C7 15 1 9 1 3z"/></svg>
        07 3964 2275
      </li>
      <li class="contact__item">
        <svg class="contact__icon" viewBox="0 0 16 16" aria-hidden="true"><path d="M1 3h14v10H1z M2 4l6 5 6-5" fill="none" stroke="#3aa3d9" stroke-width="1.6"/></svg>
        admin@harbourlightsmiles.com.au
      </li>
      <li class="contact__item">
        <svg class="contact__icon" viewBox="0 0 16 16" aria-hidden="true"><g fill="none" stroke="#3aa3d9" stroke-width="1.3"><circle cx="8" cy="8" r="6.5"/><ellipse cx="8" cy="8" rx="3" ry="6.5"/><path d="M1.5 8h13M2.5 4.5h11M2.5 11.5h11"/></g></svg>
        www.harbourlightsmiles.com.au
      </li>
      <li class="contact__item">
        <svg class="contact__icon" viewBox="0 0 16 16" aria-hidden="true"><path d="M8 1l7 6h-2v8H9.5v-5h-3v5H3V7H1z"/></svg>
        <span>S27, Level 3, Ardent North Plaza,<br>814 Tallowood Rd, Kelsey Heights, QLD 4019</span>
      </li>
    </ul>
  </section>

</body>
</html>
```